Webdesign für Automotive Engineering Webpage
Automotive Engineering - Main focus is Software Development & Embedded systems for the Automotive industry.
Like as HMI, ADAS, ECU
See Logo (PDF), example --> https://www.brantlex.com/de/de (competetor)

```html
<!DOCTYPE html>
<html lang="de">
<head>
<meta charset="utf-8">
<title>NORVANTEC – Automotive Engineering</title>
<link rel="stylesheet" href="https://fonts.googleapis.com/css2?family=Audiowide&family=Lato:wght@400;700&display=swap">
<style>
  :root {
    --navy: #0b2d5e;
    --navy-deep: #072249;
    --red: #e31d2b;
    --red-soft: rgba(220, 28, 44, 0.88);
    --white: #ffffff;
    --ink: #333b4a;
    --muted: #8a93a3;
    --heading: "Audiowide", "Arial Black", sans-serif;
    --body: "Lato", "Helvetica Neue", Arial, sans-serif;
  }
  * { box-sizing: border-box; margin: 0; padding: 0; }
  html, body { width: 1200px; height: 3098px; overflow: hidden; }
  body { position: relative; font-family: var(--body); color: var(--ink); background: var(--white); }

  .abs { position: absolute; }

  /* header */
  .menu-toggle { left: 0; top: 0; width: 83px; height: 125px; background: var(--red); }
  .menu-toggle span { position: absolute; left: 26px; width: 33px; height: 3px; background: var(--white); }
  .site-header { left: 83px; top: 0; width: 1117px; height: 125px; display: flex; align-items: center; justify-content: center; }
  .brand { text-align: center; }
  .brand-name { font-family: var(--body); font-weight: 700; font-size: 38px; letter-spacing: 3px; color: var(--navy); line-height: 1; }
  .brand-tag { font-size: 9px; color: var(--red); margin-top: 4px; }

  /* side bar */
  .sidebar { left: 0; top: 125px; width: 83px; height: 625px; background: var(--navy); }
  .sidebar svg { position: absolute; left: 29px; }
  .side-brand { position: absolute; left: 41px; top: 555px; transform: rotate(-90deg); transform-origin: left top; font-weight: 700; font-size: 22px; letter-spacing: 2px; color: var(--white); white-space: nowrap; }

  /* hero */
  .hero { left: 83px; top: 125px; width: 1117px; height: 625px;
    background: radial-gradient(ellipse at 30% 60%, #1f7fb8 0%, #123e6e 30%, #0b1f3d 65%, #0a1630 100%); }
  .hero-social { right: 82px; top: 694px; display: flex; gap: 25px; }
  .hero-social span { width: 28px; height: 28px; background: #5d6677; border-radius: 3px; display: block; }

  /* section headings */
  .section-title { font-family: var(--heading); font-size: 30px; line-height: 36px; padding-left: 28px; border-left: 5px solid var(--red); }
  .section-title .top { color: var(--navy); display: block; }
  .section-title .bottom { color: var(--red); display: block; }
  .on-dark .top { color: var(--white); }

  /* services */
  .services-title { left: 83px; top: 825px; }
  .service-card { top: 938px; width: 310px; height: 309px; background: linear-gradient(160deg, #8a96a8, #3b4658); }
  .service-card.lift { box-shadow: 0 6px 14px rgba(0,0,0,0.25); }
  .service-card .caption { position: absolute; left: 0; bottom: 0; width: 100%; height: 105px; background: var(--red-soft); padding: 16px 18px; color: var(--white); }
  .caption h3 { font-size: 14px; font-weight: 700; margin-bottom: 10px; }
  .caption p { font-size: 13px; line-height: 18px; }

  /* origin */
  .origin { left: 0; top: 1322px; width: 1200px; height: 464px; background: var(--navy); }
  .origin-car { left: 36px; top: 1533px; width: 440px; height: 187px; border-radius: 48% 52% 30% 30% / 60% 60% 40% 40%;
    background: radial-gradient(ellipse at 50% 40%, #e8303a, #a9121c 70%, #5a0a10 100%); }
  .origin-title { left: 519px; top: 1395px; }
  .origin-text { left: 519px; top: 1492px; width: 600px; color: var(--white); font-size: 13px; line-height: 18.5px; }
  .origin-text p + p, .who-text p + p { margin-top: 18px; }

  /* who */
  .who-title { left: 83px; top: 1858px; }
  .who-text { left: 83px; top: 1965px; width: 552px; font-size: 13px; line-height: 18.5px; color: var(--ink); }
  .who-photo { left: 713px; top: 1786px; width: 487px; height: 546px;
    background: linear-gradient(135deg, #1d3b5c 0%, #2f5a7e 40%, #c49a7c 70%, #44566c 100%); }

  /* contact */
  .contact { left: 0; top: 2332px; width: 1200px; height: 455px; background: var(--navy); }
  .contact-title { left: 83px; top: 2429px; }
  .contact-title .top { font-size: 30px; line-height: 36px; }
  .contact-lead { left: 100px; top: 2613px; width: 360px; color: var(--white); font-size: 13px; line-height: 18.5px; }
  .contact-form { left: 652px; top: 2434px; width: 464px; }
  .field { width: 464px; height: 39px; background: var(--white); border-radius: 2px; margin-bottom: 18px; padding: 0 12px; display: flex; align-items: center; font-size: 13px; color: var(--muted); }
  .submit { width: 183px; height: 38px; background: var(--red); color: var(--white); font-size: 12px; letter-spacing: 2px; display: flex; align-items: center; justify-content: center; border-radius: 2px; margin-top: 1px; }

  /* footer */
  .footer-brand { left: 99px; top: 2846px; }
  .footer-brand .brand-name { font-size: 34px; }
  .footer-social { left: 101px; top: 2948px; display: flex; gap: 17px; }
  .footer-social span { width: 21px; height: 21px; background: var(--navy); border-radius: 3px; display: block; }
  .footer-col h4 { font-size: 14px; font-weight: 700; color: var(--ink); margin-bottom: 14px; }
  .footer-col a { display: block; font-size: 13px; color: var(--ink); text-decoration: none; line-height: 27px; }
  .footer-contact { font-size: 11px; line-height: 19px; color: var(--ink); }
  .footer-contact .row { display: flex; gap: 12px; }
  .footer-contact svg { flex: none; margin-top: 2px; }
  .footer-contact .indent { padding-left: 28px; }
  .bottom-bar { left: 0; top: 3054px; width: 1200px; height: 44px; background: var(--red); color: var(--white); font-size: 11px; display: flex; align-items: center; justify-content: space-between; padding: 0 84px; }
</style>
</head>
<body>

  <div class="abs menu-toggle" aria-label="Menü">
    <span style="top:50px"></span><span style="top:60px"></span><span style="top:70px"></span>
  </div>

  <header class="abs site-header">
    <div class="brand">
      <div class="brand-name">NORVANTEC</div>
      <div class="brand-tag">Integrated Vehicle Engineering Services</div>
    </div>
  </header>

  <nav class="abs sidebar" aria-label="Schnellzugriff">
    <svg style="top:43px" width="24" height="24" viewBox="0 0 24 24" fill="none" stroke="#fff" stroke-width="2.4"><circle cx="10" cy="10" r="6.5"/><path d="M15 15l6 6"/></svg>
    <svg style="top:108px" width="26" height="26" viewBox="0 0 24 24" fill="none" stroke="#fff" stroke-width="1.8"><circle cx="12" cy="12" r="10"/><ellipse cx="12" cy="12" rx="4.5" ry="10"/><path d="M2 12h20M4 6.5h16M4 17.5h16"/></svg>
    <svg style="top:175px" width="24" height="24" viewBox="0 0 24 24" fill="#fff"><path d="M6.6 10.8a15 15 0 006.6 6.6l2.2-2.2a1 1 0 011-.25 11.4 11.4 0 003.6.57 1 1 0 011 1V20a1 1 0 01-1 1A17 17 0 013 4a1 1 0 011-1h3.5a1 1 0 011 1c0 1.25.2 2.45.57 3.57a1 1 0 01-.25 1z"/></svg>
    <svg style="top:238px" width="26" height="24" viewBox="0 0 26 24" fill="none" stroke="#fff" stroke-width="2"><rect x="6" y="2" width="18" height="16"/><path d="M2 6v16h18M10 7h10M10 11h10M10 15h6"/></svg>
    <div class="side-brand">NORVANTEC</div>
  </nav>

  <div class="abs hero" role="img" aria-label="Sportwagen, halb als leuchtendes blaues Drahtgittermodell, auf dunklem Technik-Hintergrund"></div>
  <div class="abs hero-social" aria-label="Soziale Netzwerke"><span></span><span></span><span></span><span></span></div>

  <section>
    <h2 class="abs section-title services-title"><span class="top">Unsere</span><span class="bottom">Leistungen</span></h2>

    <article class="abs service-card lift" style="left:83px" role="img" aria-label="Geschäftsmann berührt eine digitale Oberfläche mit vernetzten Symbolen">
      <div class="caption"><h3>Full Service Engineering</h3><p>Übernahme kompletter R&amp;D Projekte als Fremdleistung</p></div>
    </article>
    <article class="abs service-card" style="left:445px; background:linear-gradient(160deg,#e4e6ea,#8d7a62 60%,#3d3f44)" role="img" aria-label="Berater im Gespräch am Schreibtisch">
      <div class="caption"><h3>Premium Recruiting</h3><p>Vermittlung bis hin zum Onboarding von Freelancern und Festangestellten</p></div>
    </article>
    <article class="abs service-card" style="left:807px; background:linear-gradient(160deg,#dfe3e8,#7a5a45 60%,#3a2a26)" role="img" aria-label="Ingenieur an seinem Arbeitsplatz im Büro">
      <div class="caption"><h3>Arbeitnehmerüberlassung</h3><p>Automotive R&amp;D Experten und Ingenieure in Zeitarbeit</p></div>
    </article>
  </section>

  <section>
    <div class="abs origin"></div>
    <div class="abs origin-car" role="img" aria-label="Roter Sportwagen in Seitenansicht"></div>
    <h2 class="abs section-title on-dark origin-title"><span class="top">Originate in</span><span class="bottom">Engineering</span></h2>
    <div class="abs origin-text">
      <p>Halvor Recruitment vereint in sich 25 Jahre Branchen- und Projekterfahrung vom Freelance Ingenieur bis zum Task Force Manager in den Branchen Automotive, Schienenfahrzeuge, Luft- und Raumfahrt, Rüstung und Informationstechnologie.</p>
      <p>Firmengründer und Geschäftsführer Jonas Halvor kennt die Industrie seit über zwei Jahrzehnten, in denen er in Positionen als IT Entwicklungsingenieur, Experte für Geodaten und rund um das Thema autonomes Fahren und Fahrassistenzsysteme, bis zum CIO und Task Force Manager bei fast allen wichtigen OEMs und Tier1s des Automotive Sektors und anderer Schlüsselindustrien Erfahrungen sammeln konnte.</p>
      <p>Wie der Firmengründer, so verfügen auch alle maßgeblichen Mitarbeiter bei Halvor Recruitment über diese Double Qualification – wir sprechen Ihre Sprache und wissen, wo Ihr Bedarf liegt, kennen Ihre Abläufe und Prozesse, sind aus eigener Erfahrung heraus im Geschäft.</p>
    </div>
  </section>

  <section>
    <h2 class="abs section-title who-title"><span class="top">Wer wir</span><span class="bottom">sind</span></h2>
    <div class="abs who-text">
      <p>Halvor Recruitment vereint in sich 25 Jahre Branchen- und Projekterfahrung vom Freelance Ingenieur bis zum Task Force Manager in den Branchen Automotive, Schienenfahrzeuge, Luft- und Raumfahrt, Rüstung und Informationstechnologie.</p>
      <p>Firmengründer und Geschäftsführer Jonas Halvor kennt die Industrie seit über zwei Jahrzehnten, in denen er in Positionen als IT Entwicklungsingenieur, Experte für Geodaten und rund um das Thema autonomes Fahren und Fahrassistenzsysteme, bis zum CIO und Task Force Manager bei fast allen wichtigen OEMs und Tier1s des Automotive Sektors und anderer Schlüsselindustrien Erfahrungen sammeln konnte.</p>
      <p>Wie der Firmengründer, so verfügen auch alle maßgeblichen Mitarbeiter bei Halvor Recruitment über diese Double Qualification. Sie sprechen mit Fachleuten und Kollegen, nicht mit reinen Recruitern!</p>
      <p>Wir wissen, wo der Bedarf unserer Kunden liegt, kennen deren Abläufe und Prozesse, sind aus eigener Erfahrung heraus im Geschäft.</p>
    </div>
    <div class="abs who-photo" role="img" aria-label="Junger Ingenieur mit Brille vor Bildschirmen in einem Kontrollraum"></div>
  </section>

  <section>
    <div class="abs contact"></div>
    <h2 class="abs section-title on-dark contact-title"><span class="top">Sie suchen Spezialisten<br>für eine bestimmte<br>Aufgabe, oder möchten<br>mit uns in Kontakt treten?</span></h2>
    <p class="abs contact-lead">Senden Sie uns zum Beispiel Ihre Anforderungen und wir kommen mit passenden Profilen auf Sie zu, oder nehmen Sie einfach mit uns Kontakt auf und erfahren was wir für Sie tun können.</p>
    <form class="abs contact-form">
      <div class="field">Name*</div>
      <div class="field">E-Mail*</div>
      <div class="field">Telefonnummer</div>
      <div class="field">Ort/PLZ*</div>
      <div class="submit">ANFRAGE ABSENDEN</div>
    </form>
  </section>

  <footer>
    <div class="abs brand footer-brand" style="text-align:left">
      <div class="brand-name">NORVANTEC</div>
      <div class="brand-tag">Integrated Vehicle Engineering Services</div>
    </div>
    <div class="abs footer-social" aria-label="Soziale Netzwerke"><span></span><span></span><span></span><span></span></div>

    <div class="abs footer-col" style="left:386px; top:2840px">
      <h4>Navigation</h4>
      <a href="#">Über uns</a><a href="#">Unsere Leistungen</a><a href="#">Bewerber</a><a href="#">Offene Stellen</a><a href="#">Kontakt</a>
    </div>
    <div class="abs footer-col" style="left:637px; top:2840px">
      <h4>Kundenservice</h4>
      <a href="#">Registrieren</a><a href="#">Impressium</a><a href="#">Datenschutz</a>
    </div>
    <div class="abs footer-col" style="left:888px; top:2840px">
      <h4>Adresse &amp; Kontakt</h4>
      <div class="footer-contact">
        <div class="row"><svg width="16" height="16" viewBox="0 0 24 24" fill="#b7bfcc"><path d="M12 2a7 7 0 00-7 7c0 5 7 13 7 13s7-8 7-13a7 7 0 00-7-7zm0 9.5A2.5 2.5 0 1112 6a2.5 2.5 0 010 5.5z"/></svg><span>Lindenstraße 14<br>D - 34117 Brühlhausen (OT Weiden)</span></div>
        <div class="row"><svg width="16" height="16" viewBox="0 0 24 24" fill="#b7bfcc"><path d="M6.6 10.8a15 15 0 006.6 6.6l2.2-2.2a1 1 0 011-.25 11.4 11.4 0 003.6.57 1 1 0 011 1V20a1 1 0 01-1 1A17 17 0 013 4a1 1 0 011-1h3.5a1 1 0 011 1c0 1.25.2 2.45.57 3.57a1 1 0 01-.25 1z"/></svg><span>+49 (0)5512 -730 41 18</span></div>
        <div class="row" style="margin-top:4px"><svg width="16" height="16" viewBox="0 0 24 24" fill="#b7bfcc"><path d="M6 2h12v6H6zM3 9h18v9h-3v4H6v-4H3zM8 15v5h8v-5z"/></svg><span>+49 (0)5512 -730 41 19</span></div>
        <div class="row" style="margin-top:4px"><svg width="16" height="16" viewBox="0 0 24 24" fill="#b7bfcc"><path d="M2 5h20v14H2zm2 2v.5l8 5 8-5V7l-8 5z"/></svg><span>office@halvor-recruitment.de<br>D-U-N-S Nr. 512887310</span></div>
      </div>
    </div>

    <div class="abs bottom-bar"><span>© 2020 norvantec.com | All rights reserved.</span><span>TremsOfUse&nbsp; Privacy</span></div>
  </footer>

</body>
</html>
```